Book Title: “Ember: Road of Quiet Dawn” Please see the attachment “Text on the cover”.

Book Cover Design Instructions: This book is meant for people of all religions and nationalities. Therefore, on the cover, there should be no mosque or an object specific to any religion. The primary emphasis should be on the "unconditional love of God." Therefore, use universal symbols of love. The second priority themes could be Sufism, Peace, and self-improvement. Rest is your imagination. Please also see the attachment: 'Book description and author's Bio.'
This book has the potential to be a best seller. Please do a good job.
What Book Cover Formats are required: A designer should submit cover designs in three formats: (1) eBook, (2) Paperback, and (3) Hardback. These books will be published on Velmora PBX.
Format requirements for eBooks are available from: https://pbx.velmora-press.example/en_US/help/topic/R731928405.
You can find paperback and hardback cover measurements from: https://pbx.velmora-press.example/en_US/cover-calculator
• To complete the project, all three formats should be accepted by Velmora PBX.
• The book interior trim size is 6.14 X 9.21 inches.
• Interior Type: Premium color.
• No bleed.
• I do not upload barcode. So, the back cover should have room for Velmora to print the barcode.
• Number of pages 126.
Compensation for the designer: After selecting one designer, I will increase the amount by $200 on Artlumo to compensate for three deliverables.
Follow-up of the Project:
After the book is published, I may need minor revisions. For example, the number of pages may change. Therefore, I will need the same design in revised sizes. In that case, I will pay $25 for each revision. For example, if the number of pages changes, I will need a different spine for paperback and hardback, then I will pay the artist $25 + $25 = $50 for both designs.
List of Enclosers:
1. Text on the cover.
2. Book description and author's Bio for the back cover.
3. Later, I will upload my picture for the book's back cover.

Target Market(s)

Any adult

Industry/Entity Type

Any industry

Requirements
Must have
• Three Deliverables

```html
<!DOCTYPE html>
<html lang="en">
<head>
<meta charset="utf-8">
<title>Ember: Road of Quiet Dawn — Front Cover</title>
<link rel="stylesheet" href="https://fonts.googleapis.com/css2?family=Cinzel:wght@400;700;900&family=Josefin+Sans:wght@400&display=swap">
<style>
  :root {
    --page-bg: #e8dccd;
    --cover-dark: #3a1030;
    --cover-red: #8e2a22;
    --cover-orange: #e0701e;
    --cover-gold: #ffd27a;
    --cover-glow: #fff8e6;
    --sea: #6f8a86;
    --band: #7b2d33;
    --title-light: #ffffff;
    --title-shade: #bdbdbd;
    --text-white: #fbf6ee;
  }
  * { box-sizing: border-box; margin: 0; padding: 0; }
  html, body {
    width: 1200px;
    height: 1102px;
    overflow: hidden;
    background: var(--page-bg);
  }
  .cover {
    position: absolute;
    left: 278px;
    top: 30px;
    width: 644px;
    height: 1042px;
    overflow: hidden;
    background: var(--cover-red);
    box-shadow: 0 6px 18px rgba(60, 30, 10, 0.25);
  }
  .cover-art {
    position: absolute;
    inset: 0 0 58px 0;
    background:
      radial-gradient(ellipse 34% 24% at 50% 62%, var(--cover-glow) 0%, var(--cover-gold) 35%, rgba(255,160,60,0.55) 65%, rgba(224,112,30,0) 100%),
      radial-gradient(ellipse 70% 40% at 75% 18%, rgba(240,130,50,0.75) 0%, rgba(240,130,50,0) 70%),
      linear-gradient(to bottom, transparent 86%, var(--sea) 90%, #4f6663 100%),
      linear-gradient(to bottom, var(--cover-dark) 0%, #6e1d2c 22%, var(--cover-red) 45%, #b84420 70%, #9a3a22 86%);
  }
  .author {
    position: absolute;
    top: 62px;
    width: 100%;
    text-align: center;
    font-family: "Cinzel", serif;
    font-weight: 400;
    font-size: 50px;
    letter-spacing: 1px;
    color: var(--text-white);
    text-shadow: 0 2px 4px rgba(0,0,0,0.45);
  }
  .title {
    position: absolute;
    top: 150px;
    width: 100%;
    text-align: center;
    font-family: "Cinzel", serif;
    font-weight: 900;
    font-size: 140px;
    line-height: 1;
    color: var(--title-light);
    background: linear-gradient(to bottom, var(--title-light) 30%, var(--title-shade) 100%);
    -webkit-background-clip: text;
    background-clip: text;
    -webkit-text-fill-color: transparent;
    filter: drop-shadow(0 4px 5px rgba(0,0,0,0.5));
  }
  .subtitle {
    position: absolute;
    top: 318px;
    width: 100%;
    text-align: center;
    font-family: "Cinzel", serif;
    font-weight: 700;
    font-size: 44px;
    color: var(--text-white);
    text-shadow: 0 3px 5px rgba(0,0,0,0.5);
  }
  .tagline-band {
    position: absolute;
    left: 0;
    bottom: 0;
    width: 100%;
    height: 58px;
    background: var(--band);
    display: flex;
    align-items: center;
    justify-content: center;
  }
  .tagline {
    font-family: "Josefin Sans", sans-serif;
    font-size: 23px;
    color: var(--text-white);
    padding-top: 4px;
  }
</style>
</head>
<body>
  <main class="cover">
    <div class="cover-art" role="img" aria-label="Radiant glowing heart of golden light rising from a calm sea under a fiery orange and crimson sky"></div>
    <p class="author">Dr. Noor Halvani</p>
    <h1 class="title">EMBER :</h1>
    <h2 class="subtitle">Road of Quiet Dawn</h2>
    <div class="tagline-band">
      <p class="tagline">Guide to Cultivating Inner Peace and Mindful Living</p>
    </div>
  </main>
</body>
</html>
```